Plakat-Design  für Laufverein
Plakat-Design für Laufverein
Zielgruppe
Wir sind ein Laufverein der dieses Jahr zum 7. Mal eine Laufveranstaltung organisiert.
Dieses Jahr möchten wir aber neue Wege gehen.
Der Name der gesamten Veranstaltung 'Sonnhang im Schwung'
Datum der Veranstaltung ist der 21.6.2020, Beginn Kinderläufe ab 9:30 Uhr, Beginn Hauptlauf und 'Quick 2 easy Dash' 10:30 Uhr)
Die Veranstaltung besteht
- aus einem 10 KM Hauptlauf inkl. Zeitnehmung (100,00 Tagessieg Prämie für 1. Dame und 1. Herr)
- einem 'Quick 2 Easy Dash' - 5km - OHNE Zeitnehmung. Unter allen Teilnehmern wird je 1 Paar Damen- und 1 Paar Herrenlaufschuhe verlost mit der Startnummer bei der Siegerehrung )
- Kinderläuf mit 600 m
- Schülerlauf mit 1050 m
Rahmenprogramm: grosse Tombola, Ort der Veranstaltung ist das 'talstation Kolbing', Parkplätze und Duschen gratis vorhanden.
Aufgabenstellung
Logoleiste für ca. 15 Sponsoren vorsehen.
Wichtig wäre sowohl die 'ambitionierten Läufer' für den 10 KM Lauf (Preisgeld für Tagessieg M / W) sowie die Läufer die gerne in der Masse untergehen für den 'Quick 2 Easy Dash' anzusprechen. Kinder nur als Zusatzangebot.
stockbilder wenn möglich von www.bilderhafenstock.de verwenden.

```html
<!DOCTYPE html>
<html lang="de">
<head>
<meta charset="utf-8">
<title>Sonnhang im Schwung – 21.6.2020</title>
<link rel="stylesheet" href="https://fonts.googleapis.com/css2?family=Anton&family=Archivo+Black&family=Open+Sans:wght@600;700&display=swap">
<style>
:root{
  --sky:#1bb4e6;
  --sky-light:#7fd0ef;
  --sun:#ffd800;
  --sun-soft:#ffe873;
  --lime:#b5cb00;
  --white:#ffffff;
  --ink:#3a3a3a;
}
*{margin:0;padding:0;box-sizing:border-box}
html,body{width:849px;height:1200px;overflow:hidden;background:var(--white)}
.poster{position:relative;width:849px;height:1200px;overflow:hidden;background:var(--sky);font-family:"Anton",sans-serif}
.backdrop{position:absolute;left:0;top:0}
.badge{position:absolute;border-radius:50%;display:flex;flex-direction:column;align-items:center;justify-content:center;text-align:center;line-height:1}
.title{position:absolute;left:56px;top:96px;font-family:"Archivo Black",sans-serif;font-size:58px;line-height:1;color:var(--white);transform:rotate(-3.5deg);transform-origin:left bottom;white-space:nowrap;letter-spacing:-1px}
.date{position:absolute;left:352px;top:172px;font-family:"Archivo Black",sans-serif;font-size:80px;line-height:1;color:var(--sun);transform:rotate(-4deg);transform-origin:left bottom;white-space:nowrap;letter-spacing:-3px}
.badge--title{left:20px;top:-2px;width:286px;height:272px;background:var(--sun)}
.badge--prize{left:293px;top:333px;width:184px;height:184px;background:var(--lime);color:var(--white)}
.badge--prize .big{font-size:36px}
.badge--prize .small{font-size:17px;margin-top:8px}
.badge--main{left:-11px;top:376px;width:362px;height:362px;background:var(--sun);color:var(--white)}
.distance{font-size:98px}
.race{font-size:44px;margin-top:6px}
.time{font-size:21px;color:var(--sun-soft);margin-top:28px}
.note{font-family:"Open Sans",sans-serif;font-weight:700;font-size:14px;color:var(--sun-soft);margin-top:4px}
.badge--raffle{left:96px;top:702px;width:204px;height:204px;background:var(--white);padding-top:14px}
.badge--raffle .big{font-size:38px;color:var(--sky)}
.badge--raffle .small{font-size:22px;color:var(--sun);margin-top:4px}
.badge--parking{left:512px;top:436px;width:170px;height:170px;background:var(--sun);color:var(--white);font-size:22px;line-height:1.25}
.badge--kids{left:526px;top:572px;width:204px;height:204px;background:var(--sky);color:var(--white)}
.badge--kids .big{font-size:34px;line-height:1.18}
.badge--kids .small{font-size:17px;margin-top:12px}
.badge--fun{left:337px;top:710px;width:368px;height:368px;background:var(--sun);color:var(--white);justify-content:flex-start;padding-top:54px}
.badge--fun .distance{font-size:94px}
.badge--fun .race{font-size:40px}
.info-band{position:absolute;left:0;top:1016px;width:849px;height:51px;background:var(--lime);color:var(--white);font-size:21px;display:flex;align-items:center;justify-content:center}
.sponsors{position:absolute;left:0;top:1067px;width:849px;height:133px;background:var(--white);display:grid;grid-template-columns:repeat(8,1fr);align-content:center;row-gap:22px;padding:0 118px}
.sponsor{font-family:"Open Sans",sans-serif;font-weight:700;font-size:8px;color:var(--ink);text-align:center;display:flex;align-items:center;justify-content:center;gap:3px;line-height:1.1}
.sponsor i{display:inline-block;width:9px;height:9px;background:var(--sky);flex:none}
</style>
</head>
<body>
<main class="poster">
  <svg class="backdrop" width="849" height="1016" viewBox="0 0 849 1016">
    <defs>
      <linearGradient id="runner-tones" x1="0" y1="0" x2="1" y2="1">
        <stop offset="0" stop-color="#f3a45a"/>
        <stop offset="0.45" stop-color="#fde9c4"/>
        <stop offset="0.8" stop-color="#f2c98a"/>
        <stop offset="1" stop-color="#9fd6ea"/>
      </linearGradient>
    </defs>
    <polygon points="470,330 560,80 620,0 849,0 849,1016 75,1016" fill="var(--sky-light)" opacity="0.55"/>
    <polygon role="img" aria-label="Stockfoto: Läuferbeine in Laufschuhen auf sonnigem Pflaster" points="500,330 590,110 640,0 849,0 849,720 690,1016 150,1016" fill="url(#runner-tones)"/>
    <polygon points="849,380 849,1016 660,1016" fill="var(--sky)" opacity="0.6"/>
    <line x1="575" y1="330" x2="440" y2="600" stroke="var(--sky)" stroke-width="4"/>
    <line x1="432" y1="540" x2="186" y2="1016" stroke="var(--sky)" stroke-width="3"/>
    <line x1="849" y1="180" x2="700" y2="475" stroke="var(--lime)" stroke-width="4"/>
    <line x1="800" y1="370" x2="680" y2="590" stroke="var(--white)" stroke-width="3"/>
    <line x1="810" y1="408" x2="700" y2="610" stroke="var(--sky)" stroke-width="4"/>
  </svg>

  <div class="badge badge--title"></div>
  <h1 class="title">Sonnhang im Schwung</h1>
  <p class="date">21.6.2020</p>

  <div class="badge badge--raffle"><span class="big">Verlosung</span><span class="small">Laufschuhe<br>zu gewinnen</span></div>

  <div class="badge badge--main">
    <span class="distance">10 km</span>
    <span class="race">Hauptlauf</span>
    <span class="time">10:30 Uhr | talstation Kolbing</span>
    <span class="note">mit Zeitmessung</span>
  </div>

  <div class="badge badge--prize"><span class="big">Preisgeld</span><span class="small">für Tagessieg</span></div>

  <div class="badge badge--parking">Parkplätze &amp;<br>Duschen gratis<br>vorhanden</div>

  <div class="badge badge--kids"><span class="big">+ Kinder &amp;<br>Schülerlauf</span><span class="small">ab 9.30 Uhr</span></div>

  <div class="badge badge--fun">
    <span class="distance">5 km</span>
    <span class="race">Quick 2 Easy Dash</span>
    <span class="time">10:30 Uhr | talstation Kolbing</span>
    <span class="note">ohne Zeitmessung</span>
  </div>

  <p class="info-band">Infos zum Programm &amp; Anmeldung: www.sonnhang-im-schwung.at</p>

  <section class="sponsors" aria-label="Sponsoren">
    <span class="sponsor">LC Sonnhang</span>
    <span class="sponsor">Sportclub Felden</span>
    <span class="sponsor"><i></i>Talbank Sonnhang</span>
    <span class="sponsor">Kernkraft Nahrung</span>
    <span class="sponsor">Schuhwerkstatt</span>
    <span class="sponsor"><i></i>Gemeinde Kolbing</span>
    <span class="sponsor">talstation Kletterhalle</span>
    <span class="sponsor">Vitafit Sonnhang</span>
    <span class="sponsor">Sportino</span>
    <span class="sponsor">Haustechnik Brandl</span>
    <span class="sponsor">Versicherung Moser</span>
    <span class="sponsor">Sonnhang Alpin</span>
    <span class="sponsor">talstation Bistro</span>
    <span class="sponsor">Bergquell Bier</span>
    <span class="sponsor">Druckerei Lindner</span>
    <span class="sponsor">FELDKANTE</span>
  </section>
</main>
</body>
</html>
```